Cover for CD-single

MAVE is a young singer-songwriter and needs a CD cover design for her first single "Paper boats at dawn". Her song is about her best friend who recently moved from Europe to Australia with her family. But even though they now live on the other side of the world, they will always be there for each other.
You can use the picture attached or you can see it as an inspiration.
Please put the name of the artist: MAVE
and the name of the song on the cover: Paper boats at dawn

```html
<!DOCTYPE html>
<html lang="en">
<head>
<meta charset="utf-8">
<title>MAVE – Paper boats at dawn</title>
<link rel="stylesheet" href="https://fonts.googleapis.com/css2?family=Sacramento&family=Mulish:wght@400&display=swap">
<style>
  :root {
    --page-bg: #f4f4f5;
    --sky: #dcd9de;
    --haze: #bfa9b6;
    --city: #9a7c8d;
    --lake: #7f9494;
    --gravel: #7c797c;
    --gravel-dark: #5f5c5f;
    --ink-light: #ffffff;
  }
  html, body {
    margin: 0;
    padding: 0;
    width: 1200px;
    height: 1200px;
    overflow: hidden;
    background: var(--page-bg);
  }
  .cover {
    position: absolute;
    left: 100px;
    top: 100px;
    width: 1000px;
    height: 1000px;
    overflow: hidden;
    box-shadow: 0 14px 24px rgba(0, 0, 0, 0.18);
  }
  .cover-photo {
    position: absolute;
    inset: 0;
    background:
      radial-gradient(ellipse 30% 40% at 52% 72%, rgba(214, 40, 140, 0.55), rgba(214, 40, 140, 0) 70%),
      linear-gradient(180deg,
        var(--sky) 0%,
        var(--sky) 18%,
        var(--haze) 32%,
        var(--lake) 44%,
        var(--city) 55%,
        var(--gravel) 78%,
        var(--gravel-dark) 100%);
  }
  .artist-name {
    position: absolute;
    left: 0;
    right: 0;
    top: 120px;
    margin: 0;
    text-align: center;
    font-family: "Sacramento", cursive;
    font-weight: 400;
    font-size: 300px;
    line-height: 1;
    color: var(--ink-light);
  }
  .song-title {
    position: absolute;
    left: 0;
    right: 0;
    top: 895px;
    margin: 0;
    text-align: center;
    font-family: "Mulish", sans-serif;
    font-weight: 400;
    font-size: 44px;
    letter-spacing: 0.06em;
    color: var(--ink-light);
  }
</style>
</head>
<body>
  <main class="cover">
    <div class="cover-photo" role="img" aria-label="Photo: two friends hugging on a bright pink bench at a lookout above a lakeside town and mountains, seen from behind, with soft bokeh sparkles"></div>
    <h1 class="artist-name">mave</h1>
    <p class="song-title">PAPER BOATS AT DAWN</p>
  </main>
</body>
</html>
```